Business Card for my Photography/Video Business

I would like the card to say Event Photographer and Videographer. I like the Black and Gold look to it as well but open to other options. I don't want it to be super vibrant or colorful. Simple, elegant and professional

```html
<!DOCTYPE html>
<html lang="en">
<head>
<meta charset="UTF-8">
<title>Orla Studio — Business Card</title>
<link rel="stylesheet" href="https://fonts.googleapis.com/css2?family=Oswald:wght@400;500&display=swap">
<style>
  :root {
    --backdrop: #2f2723;
    --card-black: #1d1d1e;
    --card-black-light: #262627;
    --gold: #c9a42a;
  }
  * { margin: 0; padding: 0; box-sizing: border-box; }
  html, body {
    width: 1200px;
    height: 860px;
    overflow: hidden;
    background: var(--backdrop);
  }
  .canvas {
    position: relative;
    width: 1200px;
    height: 860px;
  }
  .card {
    position: absolute;
    width: 560px;
    height: 320px;
    background: linear-gradient(135deg, var(--card-black-light), var(--card-black));
    border-radius: 4px;
    box-shadow: 0 14px 30px rgba(0, 0, 0, 0.45);
  }
  .card--front {
    left: 70px;
    top: 90px;
  }
  .card--back {
    left: 570px;
    top: 450px;
  }
  .brand {
    position: absolute;
    inset: 0;
    display: flex;
    align-items: center;
    justify-content: center;
  }
  .brand__name {
    font-family: "Oswald", sans-serif;
    font-weight: 500;
    font-size: 56px;
    letter-spacing: 3px;
    color: var(--gold);
    line-height: 1;
  }
  .services {
    position: absolute;
    inset: 0;
    display: flex;
    flex-direction: column;
    align-items: center;
    justify-content: center;
    gap: 10px;
    font-family: "Oswald", sans-serif;
    font-weight: 500;
    font-size: 24px;
    letter-spacing: 4px;
    color: var(--gold);
    text-transform: uppercase;
    text-align: center;
  }
</style>
</head>
<body>
  <main class="canvas">
    <section class="card card--front">
      <div class="brand">
        <span class="brand__name">Orla Studio</span>
      </div>
    </section>
    <section class="card card--back">
      <div class="services">
        <p class="services__line">Event Photographer</p>
        <p class="services__divider">-</p>
        <p class="services__line">Videographer</p>
      </div>
    </section>
  </main>
</body>
</html>
```